Buss cards
Stationary & envelops
Buss cards - Transportation
Creative Brief
Simple
Harbor Crest Moving
412 West 57th Avenue Brooklyn, NY 11204
Info@Harborcrestmoving.example
www.harborcrestmoving.example
US DOT # 4718392
this is a moving company, that relocates household goods, any ideas you may have would be appreciated
Local & Long Distance Residential & Commercial Storage Facility visit us online: www.harborcrestmoving.example

```html
<!DOCTYPE html>
<html lang="en">
<head>
<meta charset="utf-8">
<title>Harbor Crest Moving – Stationery Package</title>
<link rel="stylesheet" href="https://fonts.googleapis.com/css2?family=Roboto:wght@400;700;900&display=swap">
<style>
:root{
  --board:#efefef;
  --paper:#ffffff;
  --blue:#1f4e9e;
  --blue-light:#3b78c9;
  --orange:#f2901e;
  --orange-light:#f7b04a;
  --ink:#5a5a5a;
  --ink-soft:#9a9a9a;
}
*{margin:0;padding:0;box-sizing:border-box}
html,body{width:1200px;height:569px;overflow:hidden}
body{background:var(--board);font-family:"Roboto",Arial,sans-serif;color:var(--ink);position:relative}

.package-tab{position:absolute;left:0;top:0;width:20px;height:132px;background:var(--orange)}
.package-tab span{position:absolute;left:50%;top:50%;transform:translate(-50%,-50%) rotate(-90deg);white-space:nowrap;color:#fff;font-size:10px;letter-spacing:.5px}

.brand{display:flex;align-items:center;gap:.35em;font-weight:900;color:var(--blue);text-transform:uppercase;white-space:nowrap;line-height:1}
.brand .dot{width:.8em;height:.8em;border-radius:50%;background:var(--orange);flex:none}
.brand-hero{position:absolute;left:30px;top:20px;font-size:24px}

.sheet{position:absolute;background:var(--paper);box-shadow:0 1px 3px rgba(0,0,0,.18);overflow:hidden}

/* business cards */
.card{width:92px;height:54px;left:26px}
.card-front{top:183px}
.card-back{top:250px}
.card .brand{position:absolute;left:6px;top:7px;font-size:6.5px}
.card .details{position:absolute;font-size:2.8px;line-height:1.35;color:var(--ink);white-space:nowrap}
.card-front .details{right:5px;top:27px;text-align:right}
.card-back .details{left:6px;top:29px}
.card .holder{position:absolute;left:6px;top:17px;font-size:3.6px;line-height:1.35}
.card .holder b{color:var(--blue)}
.card svg{position:absolute;left:0;bottom:0;width:100%;height:8px}

/* letterheads */
.letter{width:212px;height:268px;top:104px}
.letter-one{left:126px}
.letter-two{left:382px}
.letter .brand{position:absolute;left:12px;top:12px;font-size:10px}
.letter .body{position:absolute;left:14px;right:14px;top:50px;font-size:3.6px;line-height:1.6;color:var(--ink)}
.letter .body h3{font-size:4.6px;color:#333;margin-bottom:1px}
.letter .body .date{margin-bottom:5px;color:var(--ink-soft)}
.letter .body p{margin-bottom:5px}
.letter .sign{margin-top:10px}
.letter .sign b{display:block;color:#333}
.letter .footer{position:absolute;left:0;bottom:0;width:100%;height:50px}
.letter .contact{position:absolute;right:10px;bottom:4px;text-align:right;font-size:3.2px;line-height:1.45;color:#fff;white-space:nowrap}

/* envelopes */
.envelope{width:212px;height:62px;left:620px}
.env-orange{top:130px}
.env-blue{top:198px;background:var(--blue)}
.env-white{top:266px}
.envelope svg{position:absolute;left:0;top:0;width:100%;height:100%}
.env-white .brand{position:absolute;left:10px;top:9px;font-size:8px}
.env-white .details{position:absolute;left:10px;top:21px;font-size:3.2px;line-height:1.45}
</style>
</head>
<body>

<div class="package-tab"><span>stationary package</span></div>

<div class="brand brand-hero"><span class="dot"></span>Harbor Crest Moving</div>

<!-- business cards -->
<div class="sheet card card-front">
  <div class="brand"><span class="dot"></span>Harbor Crest Moving</div>
  <div class="details">Local &amp; Long Distance<br>Residential &amp; Commercial<br>Storage Facility</div>
  <svg viewBox="0 0 92 8" preserveAspectRatio="none" aria-hidden="true">
    <path d="M0 3 Q46 -1 92 4 L92 8 L0 8Z" fill="var(--orange)"/>
    <path d="M0 5 Q46 1 92 6 L92 8 L0 8Z" fill="var(--blue)"/>
  </svg>
</div>
<div class="sheet card card-back">
  <div class="brand"><span class="dot"></span>Harbor Crest Moving</div>
  <div class="holder"><b>Daniel Reyes</b><br>Operations Manager</div>
  <div class="details">412 West 57th Avenue Brooklyn, NY 11204<br>Info@Harborcrestmoving.example<br>www.harborcrestmoving.example<br>US DOT # 4718392</div>
  <svg viewBox="0 0 92 8" preserveAspectRatio="none" aria-hidden="true">
    <path d="M0 5 Q46 1 92 5 L92 8 L0 8Z" fill="var(--blue)"/>
  </svg>
</div>

<!-- letterheads -->
<div class="sheet letter letter-one">
  <div class="brand"><span class="dot"></span>Harbor Crest Moving</div>
  <div class="body">
    <h3>Dear Customer</h3>
    <div class="date">August 12</div>
    <p>Thank you for choosing us for your upcoming move. Our crew will arrive on the scheduled date with blankets, boxes and a fully equipped truck to pack, load and deliver your household goods safely.</p>
    <p>Please review the attached estimate and confirm the pickup window at least two days in advance. We look forward to making your relocation simple and stress free.</p>
    <div class="sign">Sincerely,<b>Operations Manager</b></div>
  </div>
  <svg class="footer" viewBox="0 0 212 50" preserveAspectRatio="none" aria-hidden="true">
    <path d="M0 14 Q110 0 212 8 L212 50 L0 50Z" fill="var(--orange)"/>
    <path d="M0 20 Q110 6 212 14 L212 50 L0 50Z" fill="var(--blue)"/>
  </svg>
  <div class="contact">412 West 57th Avenue Brooklyn, NY 11204<br>Info@Harborcrestmoving.example<br>www.harborcrestmoving.example<br>US DOT # 4718392</div>
</div>

<div class="sheet letter letter-two">
  <div class="brand"><span class="dot"></span>Harbor Crest Moving</div>
  <div class="body">
    <h3>Dear Customer</h3>
    <div class="date">August 12</div>
    <p>Thank you for choosing us for your upcoming move. Our crew will arrive on the scheduled date with blankets, boxes and a fully equipped truck to pack, load and deliver your household goods safely.</p>
    <p>Please review the attached estimate and confirm the pickup window at least two days in advance. We look forward to making your relocation simple and stress free.</p>
    <div class="sign">Sincerely,<b>Operations Manager</b></div>
  </div>
  <svg class="footer" viewBox="0 0 212 50" preserveAspectRatio="none" aria-hidden="true">
    <path d="M0 4 Q100 14 212 6 L212 50 L0 50Z" fill="var(--orange)"/>
    <path d="M0 9 Q100 19 212 11 L212 50 L0 50Z" fill="var(--blue)"/>
  </svg>
  <div class="contact">412 West 57th Avenue Brooklyn, NY 11204<br>Info@Harborcrestmoving.example<br>www.harborcrestmoving.example<br>US DOT # 4718392</div>
</div>

<!-- envelopes -->
<div class="sheet envelope env-orange">
  <svg viewBox="0 0 212 62" preserveAspectRatio="none" aria-hidden="true">
    <path d="M0 0 L212 0 L212 18 Q106 34 0 18Z" fill="var(--orange)"/>
    <path d="M0 18 Q106 34 212 18" fill="none" stroke="var(--orange-light)" stroke-width="1.5"/>
  </svg>
</div>
<div class="sheet envelope env-blue">
  <svg viewBox="0 0 212 62" preserveAspectRatio="none" aria-hidden="true">
    <path d="M0 0 L106 34 L212 0Z" fill="var(--blue-light)"/>
  </svg>
</div>
<div class="sheet envelope env-white">
  <svg viewBox="0 0 212 62" preserveAspectRatio="none" aria-hidden="true">
    <path d="M0 50 Q110 36 212 44 L212 62 L0 62Z" fill="var(--orange)"/>
    <path d="M0 54 Q110 42 212 50 L212 62 L0 62Z" fill="var(--blue)"/>
  </svg>
  <div class="brand"><span class="dot"></span>Harbor Crest Moving</div>
  <div class="details">412 West 57th Avenue Brooklyn, NY 11204<br>www.harborcrestmoving.example</div>
</div>

</body>
</html>
```